Update New Business Card - For Start Up

I need to update my business card, I have our old version for example. I would like to keep to the same colors and theme. We are a threat reporting and case management tool for corporations and educational institutions.

Target Market(s)

Corporate Security and Human Resources, School Administrators and Superintendents.

Industry/Entity Type

Physical Security and Technology.

Contact Information for Business Card

My Name, Founder/CEO, phone number 555-214-6082, Logo, Web...

Colors
0054AA
0677BA
7BADD7
CADEEF
E8F1F8

Requirements
Must have
• Something new and trendy.

```html
<!DOCTYPE html>
<html lang="en">
<head>
<meta charset="utf-8">
<title>Vantrel Business Card</title>
<link rel="stylesheet" href="https://fonts.googleapis.com/css2?family=Rubik:wght@400;500&display=swap">
<style>
  :root {
    --page: #e3e3e3;
    --card-dark: #1b1c1e;
    --card-blue: #1e75bb;
    --accent-blue: #1e75bb;
    --text-muted: #b9b9b9;
    --mark-light: #d9dadc;
    --wordmark: #1c2633;
  }
  * { margin: 0; padding: 0; box-sizing: border-box; }
  html, body { width: 1200px; height: 1200px; overflow: hidden; background: var(--page); }
  body { position: relative; font-family: "Rubik", sans-serif; }

  .card {
    position: absolute;
    left: 262px;
    width: 686px;
    height: 392px;
    border-radius: 24px;
    overflow: hidden;
  }
  .card--front { top: 165px; background: var(--card-dark); }
  .card--back { top: 653px; background: var(--card-blue); }

  .contact-block { position: absolute; left: 62px; top: 221px; }
  .person-name {
    font-size: 22px;
    font-weight: 500;
    letter-spacing: 0.5px;
    color: var(--accent-blue);
    line-height: 1;
  }
  .person-title {
    margin-top: 6px;
    font-size: 15px;
    color: var(--text-muted);
    letter-spacing: 0.3px;
  }
  .contact-list { list-style: none; margin-top: 14px; }
  .contact-list li {
    display: flex;
    align-items: center;
    gap: 8px;
    font-size: 15px;
    color: var(--text-muted);
    letter-spacing: 0.3px;
    height: 19.5px;
  }
  .contact-list svg { width: 13px; height: 13px; flex: none; }

  .decor-circle {
    position: absolute;
    left: 323px;
    top: 34px;
    width: 330px;
    height: 330px;
    border-radius: 50%;
    background: linear-gradient(90deg, #5a5b5e 0%, #2a2b2d 45%, #080808 100%);
  }

  .brand-lockup {
    position: absolute;
    left: 124px;
    top: 151px;
    display: flex;
    align-items: center;
    gap: 18px;
  }
  .brand-dot {
    width: 90px;
    height: 90px;
    border-radius: 50%;
    background: var(--mark-light);
  }
  .brand-name {
    font-size: 52px;
    font-weight: 400;
    letter-spacing: 10px;
    color: var(--wordmark);
    line-height: 1;
  }
</style>
</head>
<body>
  <section class="card card--front">
    <div class="contact-block">
      <h1 class="person-name">THEO MARLOW</h1>
      <p class="person-title">Founder/CEO</p>
      <ul class="contact-list">
        <li>
          <svg viewBox="0 0 16 16" fill="none" stroke="#1e75bb" stroke-width="1.3"><path d="M3 1.5l3 3-1.6 1.8c.9 2 2.3 3.4 4.3 4.3L10.5 9l3 3-2 2.2C6.5 13.5 2.5 9.5 1 4.5z"/></svg>
          555-214-6082
        </li>
        <li>
          <svg viewBox="0 0 16 16" fill="none" stroke="#1e75bb" stroke-width="1.3"><rect x="1.5" y="3.5" width="13" height="9"/><path d="M1.5 3.5L8 9l6.5-5.5"/></svg>
          theo@vantrel.co
        </li>
        <li>
          <svg viewBox="0 0 16 16" fill="none" stroke="#1e75bb" stroke-width="1.3"><circle cx="8" cy="8" r="6.5"/><path d="M1.5 8h13M8 1.5c2 2 2 11 0 13M8 1.5c-2 2-2 11 0 13"/></svg>
          vantrel.co
        </li>
      </ul>
    </div>
    <div class="decor-circle"></div>
  </section>

  <section class="card card--back">
    <div class="brand-lockup">
      <div class="brand-dot"></div>
      <span class="brand-name">VANTREL</span>
    </div>
  </section>
</body>
</html>
```